Label for moisturizing face lotion - skin care

I need a label for a face moisturizer. Please see the details in the attachments. I also attached two variations of the logo.
The fonts are Futura PT for body
Orpheus Pro for header

We are looking for something very modern, simple, just black and white. It's an all natural product.
Please add under the logo:
with Phytoplankton extract and hyaluronic acid

Target Market(s)

Women

Industry/Entity Type

Skin care

Font styles to use
Sans Serif
Other font styles liked:
• Futura PT for body Orpheus Pro for header

Colors

Designer to choose only greyscale colors for use in the design.

Requirements
Nice to have
• White label with black letters, simple, clean, no serifs

```html
<!DOCTYPE html>
<html lang="en">
<head>
<meta charset="UTF-8">
<title>VELA Anti-Aging Moisturizer Label</title>
<link rel="stylesheet" href="https://fonts.googleapis.com/css2?family=Cormorant+Garamond:wght@400;500&family=Jost:wght@400;500&display=swap">
<style>
  :root {
    --paper: #ffffff;
    --ink: #111111;
    --ink-soft: #2a2a2a;
  }
  html, body {
    margin: 0;
    padding: 0;
    width: 1200px;
    height: 1200px;
    overflow: hidden;
    background: var(--paper);
  }
  .label {
    position: relative;
    width: 1200px;
    height: 1200px;
    background: var(--paper);
    color: var(--ink);
  }
  .label > * {
    margin: 0;
  }
  .brand {
    position: absolute;
    top: 522px;
    left: 0;
    width: 1200px;
    display: flex;
    justify-content: center;
    align-items: center;
    gap: 12px;
  }
  .brand-dot {
    width: 18px;
    height: 18px;
    border: 1.5px solid var(--ink);
    border-radius: 50%;
    box-sizing: border-box;
  }
  .brand-name {
    font-family: "Jost", sans-serif;
    font-weight: 400;
    font-size: 26px;
    line-height: 34px;
    letter-spacing: 6px;
    text-transform: uppercase;
    color: var(--ink);
  }
  .maker {
    position: absolute;
    top: 600px;
    left: 0;
    width: 1200px;
    text-align: center;
    font-family: "Jost", sans-serif;
    font-size: 11px;
    line-height: 14px;
    letter-spacing: 3.5px;
    color: var(--ink-soft);
  }
  .product-name {
    position: absolute;
    top: 628px;
    left: 0;
    width: 1200px;
    text-align: center;
    font-family: "Cormorant Garamond", serif;
    font-weight: 400;
    font-size: 150px;
    line-height: 1;
    letter-spacing: 24px;
    text-indent: 24px;
    color: var(--ink);
  }
  .product-type {
    position: absolute;
    top: 772px;
    left: 0;
    width: 1200px;
    text-align: center;
    font-family: "Jost", sans-serif;
    font-weight: 400;
    font-size: 24px;
    line-height: 28px;
    letter-spacing: 2.6px;
    color: var(--ink);
  }
  .divider {
    position: absolute;
    top: 817px;
    left: 452px;
    width: 296px;
    height: 3px;
    background: var(--ink);
  }
  .ingredients {
    position: absolute;
    top: 838px;
    left: 0;
    width: 1200px;
    text-align: center;
    font-family: "Jost", sans-serif;
    font-size: 12.5px;
    line-height: 20px;
    letter-spacing: 3px;
    color: var(--ink-soft);
  }
</style>
</head>
<body>
  <main class="label">
    <div class="brand">
      <span class="brand-dot"></span>
      <span class="brand-name">Marevie</span>
    </div>
    <div class="maker">BY. DR SOLEN</div>
    <h1 class="product-name">VELA</h1>
    <div class="product-type">ANTI-AGING MOISTURIZER</div>
    <div class="divider"></div>
    <p class="ingredients">WITH PHYTOPLANKTON EXTRACT<br>AND HYALURONIC ACID</p>
  </main>
</body>
</html>
```